TERRAVOL " need somthing eye catching and envirnmental friendely materials

Business Card " UNIQUE..
- use the agreed on logo.
- use wooden background.
- the environmental sound should be HIGH.

Company slogan is ZERO DISCHARGE.
We work in deploying the latest technology “ USA & Europe” in the field of drill cutting recycle and economically managing the footprint.
With the ramp up in oil demands and the increase in oil prices , operators are extending their operations into new geographical areas “ government regulations and eco-sounds” created the need to a specialty services and products that should go parallel or even ahead.

Target Market(s)

OIL field and environmental concerned.
Mainly ENGINEERS.

Industry/Entity Type

Government

Font styles to use
Decorative
Script

Colors

Designer to choose colors to be used in the design.

Requirements
Must have
• Eco - sounded.

```html
<!DOCTYPE html>
<html lang="en">
<head>
<meta charset="utf-8">
<title>TERRAVOL Business Card</title>
<link rel="stylesheet" href="https://fonts.googleapis.com/css2?family=Courgette&family=Rubik+Dirt&display=swap">
<style>
  :root {
    --page-bg: #e9e9e9;
    --wall-top: #8a4a22;
    --wall-mid: #a35a2a;
    --wall-low: #7a3e1c;
    --deck-top: #4a2412;
    --deck-low: #2e160a;
    --light-wood-a: #d9b47a;
    --light-wood-b: #b98a4c;
    --light-wood-c: #8f6432;
    --leaf-green: #5fb133;
    --ink-white: #ffffff;
    --ink-dark: #2a1a0e;
    --card-shadow: rgba(0, 0, 0, 0.35);
  }
  * { margin: 0; padding: 0; box-sizing: border-box; }
  html, body {
    width: 1200px;
    height: 1150px;
    overflow: hidden;
    background: var(--page-bg);
  }
  .canvas {
    position: relative;
    width: 1200px;
    height: 1150px;
  }
  .card {
    position: absolute;
    left: 150px;
    width: 900px;
    height: 500px;
    overflow: hidden;
    box-shadow: 0 12px 28px var(--card-shadow);
  }
  .card-front { top: 60px; }
  .card-back { top: 590px; }

  /* front */
  .wall-texture {
    position: absolute;
    inset: 0 0 45% 0;
    background: linear-gradient(90deg, var(--wall-low), var(--wall-mid) 35%, var(--wall-top) 60%, var(--wall-mid) 85%, var(--wall-low));
  }
  .deck-texture {
    position: absolute;
    inset: 55% 0 0 0;
    background: linear-gradient(180deg, var(--deck-top), var(--deck-low));
  }
  .brand {
    position: absolute;
    top: 90px;
    left: 0;
    width: 100%;
    display: flex;
    justify-content: center;
    align-items: center;
    gap: 14px;
  }
  .brand-dot {
    width: 26px;
    height: 26px;
    border-radius: 50%;
    background: var(--leaf-green);
  }
  .brand-name {
    font-family: "Courgette", cursive;
    font-size: 52px;
    color: var(--leaf-green);
    letter-spacing: 2px;
  }
  .person-name {
    position: absolute;
    top: 262px;
    left: 0;
    width: 100%;
    text-align: center;
    font-family: "Rubik Dirt", sans-serif;
    font-size: 58px;
    letter-spacing: 4px;
    color: var(--ink-white);
  }
  .person-title {
    position: absolute;
    top: 338px;
    left: 190px;
    font-family: "Courgette", cursive;
    font-size: 34px;
    color: var(--ink-white);
  }
  .contact {
    position: absolute;
    font-family: "Courgette", cursive;
    color: var(--ink-white);
  }
  .contact-web { top: 360px; right: 70px; font-size: 20px; }
  .contact-mail { top: 430px; left: 50px; font-size: 26px; }
  .contact-cell { top: 432px; left: 360px; font-size: 23px; }

  /* back */
  .light-wood-texture {
    position: absolute;
    inset: 0;
    background: linear-gradient(160deg, var(--light-wood-a), var(--light-wood-b) 55%, var(--light-wood-c));
  }
  .back-brand {
    position: absolute;
    top: 170px;
    left: 0;
    width: 100%;
    display: flex;
    justify-content: center;
    align-items: center;
    gap: 14px;
  }
  .slogan {
    position: absolute;
    top: 300px;
    left: 0;
    width: 100%;
    text-align: center;
    font-family: "Courgette", cursive;
    font-size: 40px;
    color: var(--ink-dark);
  }
</style>
</head>
<body>
  <main class="canvas">
    <section class="card card-front">
      <div class="wall-texture" role="img" aria-label="Vertical reddish-brown wooden wall grain"></div>
      <div class="deck-texture" role="img" aria-label="Dark wooden deck planks receding into perspective"></div>
      <div class="brand">
        <span class="brand-dot"></span>
        <span class="brand-name">TERRAVOL</span>
      </div>
      <h1 class="person-name">KARIM SALEH NADER</h1>
      <p class="person-title">Chief Executive Officer</p>
      <p class="contact contact-web">www.TERRAVOL.ae</p>
      <p class="contact contact-mail">IT@TERRAVOL.com</p>
      <p class="contact contact-cell">Cell 009715 555 012 34</p>
    </section>

    <section class="card card-back">
      <div class="light-wood-texture" role="img" aria-label="Light natural wooden deck planks in perspective"></div>
      <div class="back-brand">
        <span class="brand-dot"></span>
        <span class="brand-name">TERRAVOL</span>
      </div>
      <p class="slogan">Zero Discharge</p>
    </section>
  </main>
</body>
</html>
```